Business Cards

Business card design for my company.
I would like the card's background colour to be black. You can also see our web site to get an idea of our brand. https://www.dlqmarrowfield.com.au/
- Name
- Email

```html
<!DOCTYPE html>
<html lang="en">
<head>
<meta charset="utf-8">
<title>DLQ Marrowfield – Business Cards</title>
<link rel="stylesheet" href="https://fonts.googleapis.com/css2?family=Nunito+Sans:wght@400;600;700&display=swap">
<style>
  :root {
    --stage: #2b2c2e;
    --card: #3a3b3d;
    --white: #f2f2f2;
    --muted: #d6d6d6;
    --green: #2f9a45;
    --line: #cfcfcf;
  }
  * { box-sizing: border-box; margin: 0; padding: 0; }
  html, body {
    width: 1200px; height: 1153px; overflow: hidden;
    background: var(--stage);
    font-family: "Nunito Sans", Arial, sans-serif;
  }
  .card {
    position: absolute; left: 204px; width: 796px; height: 436px;
    background: var(--card);
    box-shadow: 0 10px 24px rgba(0,0,0,.45);
  }
  .card--front { top: 98px; }
  .card--back { top: 582px; }

  .person { position: absolute; left: 51px; top: 48px; }
  .person__name { font-size: 31px; font-weight: 400; color: var(--white); line-height: 1; }
  .person__first { color: var(--green); }
  .person__role { margin-top: 6px; font-size: 17px; color: var(--muted); }

  .brand-mini {
    position: absolute; right: 42px; top: 56px;
    display: flex; align-items: center; gap: 8px;
    font-size: 17px; font-weight: 700; color: var(--white);
  }
  .brand-mini__square { width: 12px; height: 12px; background: var(--green); }

  .divider { position: absolute; left: 51px; right: 42px; top: 301px; height: 2px; background: var(--line); opacity: .85; }
  .divider__accent { position: absolute; left: 51px; top: 299px; width: 118px; height: 5px; background: var(--white); }

  .contacts { position: absolute; left: 51px; top: 332px; list-style: none; }
  .contacts li {
    display: flex; align-items: center; gap: 14px;
    font-size: 17px; color: var(--muted); height: 23px;
  }
  .contacts svg { width: 14px; height: 14px; fill: var(--green); flex: none; }

  .brand-main {
    position: absolute; left: 0; right: 0; top: 168px;
    display: flex; justify-content: center; align-items: center; gap: 18px;
    font-size: 58px; font-weight: 700; color: var(--white); line-height: 1;
  }
  .brand-main__square { width: 30px; height: 30px; background: var(--green); }

  .site {
    position: absolute; left: 40px; right: 40px; top: 382px;
    display: flex; align-items: center; gap: 14px;
    font-size: 19px; color: var(--white);
  }
  .site__rule { flex: 1; height: 2px; background: var(--line); opacity: .85; }
  .site__domain { color: var(--green); }
</style>
</head>
<body>
  <section class="card card--front">
    <div class="person">
      <h1 class="person__name"><span class="person__first">Reid</span> Callum</h1>
      <p class="person__role">General Manager</p>
    </div>
    <div class="brand-mini"><span class="brand-mini__square"></span>DLQ Marrowfield</div>

    <div class="divider"></div>
    <div class="divider__accent"></div>

    <ul class="contacts">
      <li>
        <svg viewBox="0 0 24 24" aria-hidden="true"><path d="M6.6 10.8a15.1 15.1 0 0 0 6.6 6.6l2.2-2.2a1 1 0 0 1 1-.25 11.4 11.4 0 0 0 3.6.57 1 1 0 0 1 1 1V20a1 1 0 0 1-1 1A17 17 0 0 1 3 4a1 1 0 0 1 1-1h3.5a1 1 0 0 1 1 1c0 1.25.2 2.45.57 3.57a1 1 0 0 1-.25 1z"/></svg>
        0400 555 017
      </li>
      <li>
        <svg viewBox="0 0 24 24" aria-hidden="true"><path d="M2 5h20v14H2z"/></svg>
        info@dlqmarrowfield.com.au
      </li>
      <li>
        <svg viewBox="0 0 24 24" aria-hidden="true"><path d="M12 2a7 7 0 0 0-7 7c0 5.2 7 13 7 13s7-7.8 7-13a7 7 0 0 0-7-7zm0 9.5A2.5 2.5 0 1 1 12 6.5a2.5 2.5 0 0 1 0 5z"/></svg>
        Devonport, Tasmania, Australia
      </li>
    </ul>
  </section>

  <section class="card card--back">
    <div class="brand-main"><span class="brand-main__square"></span>DLQ Marrowfield</div>
    <div class="site">
      <span class="site__rule"></span>
      <span>www.<span class="site__domain">dlqmarrowfield</span>.com</span>
      <span class="site__rule"></span>
    </div>
  </section>
</body>
</html>
```